Valve bag design

I need a valve bag for 25kg wall putty bag

Here are attached bags for reference

Most of the words or design you can copy from mablunt bag attached and company profile
Also I have attached our local product for reference

```html
<!DOCTYPE html>
<html lang="en">
<head>
<meta charset="utf-8">
<title>Nova Coat Wall Putty 25kg Valve Bag</title>
<link rel="stylesheet" href="https://fonts.googleapis.com/css2?family=Anton&family=Work+Sans:wght@400;700&display=swap">
<style>
  :root {
    --navy: #181838;
    --orange: #f9ae40;
    --white: #ffffff;
    --badge-blue: #062f63;
  }
  html, body { margin: 0; padding: 0; overflow: hidden; }
  body { width: 1200px; height: 1200px; background: var(--white); }
  .bag {
    position: relative;
    width: 1200px;
    height: 1200px;
    overflow: hidden;
    background: var(--white);
    font-family: "Work Sans", Arial, sans-serif;
    color: var(--navy);
  }
  .bag__backdrop { position: absolute; inset: 0; }
  .side-band {
    position: absolute;
    top: 0;
    width: 200px;
    height: 1200px;
    background: var(--navy);
  }
  .side-band--left { left: 0; }
  .side-band--right { right: 0; }
  .side-band__name {
    position: absolute;
    font-family: "Anton", Impact, sans-serif;
    font-size: 66px;
    line-height: 1;
    letter-spacing: 1px;
    white-space: nowrap;
    width: 320px;
    text-align: center;
  }
  .side-band--left .side-band__name {
    left: 104px;
    color: var(--white);
    transform: translate(-50%, -50%) rotate(-90deg);
  }
  .side-band--right .side-band__name {
    left: 96px;
    color: var(--orange);
    transform: translate(-50%, -50%) rotate(90deg);
  }
  .brand-title {
    position: absolute;
    left: 200px;
    width: 800px;
    top: 74px;
    margin: 0;
    text-align: center;
    font-family: "Anton", Impact, sans-serif;
    font-weight: 400;
    font-size: 104px;
    line-height: 1;
    letter-spacing: 1px;
    color: var(--navy);
  }
  .product-points {
    position: absolute;
    left: 262px;
    top: 232px;
    margin: 0;
    padding: 0;
    list-style: none;
    font-weight: 700;
    font-size: 29px;
    line-height: 53px;
  }
  .product-points li { position: relative; padding-left: 36px; }
  .product-points li::before {
    content: "★";
    position: absolute;
    left: 0;
    top: -2px;
    color: var(--orange);
    font-size: 20px;
  }
  .features-heading {
    position: absolute;
    left: 272px;
    top: 528px;
    margin: 0;
    font-family: "Anton", Impact, sans-serif;
    font-weight: 400;
    font-size: 82px;
    line-height: 94px;
    color: var(--navy);
    letter-spacing: 0.5px;
  }
  .features-panel {
    position: absolute;
    left: 253px;
    top: 723px;
    width: 714px;
    height: 327px;
    background: var(--navy);
    border-radius: 38px;
  }
  .features-list {
    position: absolute;
    left: 306px;
    top: 742px;
    margin: 0;
    padding: 0;
    list-style: none;
    color: var(--white);
    font-size: 27px;
    font-weight: 400;
    line-height: 39.6px;
  }
  .features-list li { position: relative; padding-left: 45px; }
  .features-list li svg { position: absolute; left: 0; top: 12px; }
  .check-column {
    position: absolute;
    left: 826px;
    top: 663px;
    width: 84px;
    height: 445px;
    box-sizing: border-box;
    background: var(--navy);
    border-radius: 22px;
    padding: 7px;
    display: flex;
    flex-direction: column;
    justify-content: space-between;
  }
  .check-column__box {
    height: 70px;
    background: var(--white);
    border-radius: 12px;
  }
  .maker-line {
    position: absolute;
    left: 262px;
    top: 1080px;
    height: 78px;
    display: flex;
    align-items: center;
    color: var(--white);
  }
  .maker-line__label { font-size: 20px; font-weight: 400; }
  .maker-line__divider {
    width: 2px;
    height: 78px;
    background: var(--white);
    margin: 0 22px 0 26px;
  }
  .maker-line__name {
    font-family: "Anton", Impact, sans-serif;
    font-size: 48px;
    line-height: 1;
    letter-spacing: 0.5px;
  }
</style>
</head>
<body>
<main class="bag">
  <svg class="bag__backdrop" width="1200" height="1200" viewBox="0 0 1200 1200" aria-hidden="true">
    <!-- top-right swoosh -->
    <path d="M562 0 C700 60 820 190 1000 245 L1000 0 Z" fill="var(--orange)"/>
    <!-- lower wave -->
    <path d="M200 489 C420 540 560 640 700 720 C800 775 900 820 1000 836 L1000 1200 L200 1200 Z" fill="var(--orange)"/>
    <!-- swoosh behind badge -->
    <path d="M860 520 C920 522 965 519 1000 517 L1000 578 C960 580 910 580 860 574 Z" fill="var(--orange)"/>
    <!-- arrow from badge -->
    <path d="M770 505 C720 495 650 470 672 476 L693 461 L635 451 C645 470 655 485 667 498 L668 476 C700 497 740 520 770 530 Z" fill="var(--orange)"/>
    <path d="M775 495 C730 485 700 475 668 462 L668 478 C705 500 740 518 775 528 Z" fill="var(--orange)"/>
    <!-- certification badge, plain -->
    <circle cx="836" cy="533" r="90" fill="var(--orange)"/>
    <circle cx="836" cy="533" r="79" fill="none" stroke="var(--badge-blue)" stroke-width="2"/>
    <circle cx="836" cy="533" r="45" fill="var(--badge-blue)"/>
  </svg>

  <aside class="side-band side-band--left">
    <span class="side-band__name" style="top:217px">NOVA COAT</span>
    <span class="side-band__name" style="top:598px">NOVA COAT</span>
    <span class="side-band__name" style="top:980px">NOVA COAT</span>
  </aside>
  <aside class="side-band side-band--right">
    <span class="side-band__name" style="top:215px">NOVA COAT</span>
    <span class="side-band__name" style="top:597px">NOVA COAT</span>
    <span class="side-band__name" style="top:978px">NOVA COAT</span>
  </aside>

  <h1 class="brand-title">NOVA COAT</h1>

  <ul class="product-points">
    <li>Wall putty</li>
    <li>White base cement putty</li>
    <li>Premium wall putty to use for cement based<br>plaster &amp; concrete surface before paint</li>
    <li>NET WEIGHT 25kg</li>
  </ul>

  <h2 class="features-heading">TOP QUANTIES<br>&amp; FEATURES</h2>

  <div class="features-panel"></div>
  <ul class="features-list">
    <li><svg width="22" height="16" viewBox="0 0 22 16"><path d="M0 6h12V0l10 8-10 8v-6H0z" fill="var(--orange)"/></svg>Very smooth and glossy finish</li>
    <li><svg width="22" height="16" viewBox="0 0 22 16"><path d="M0 6h12V0l10 8-10 8v-6H0z" fill="var(--orange)"/></svg>Suitable for all cement surfaces</li>
    <li><svg width="22" height="16" viewBox="0 0 22 16"><path d="M0 6h12V0l10 8-10 8v-6H0z" fill="var(--orange)"/></svg>Suitable for interior &amp; exterior</li>
    <li><svg width="22" height="16" viewBox="0 0 22 16"><path d="M0 6h12V0l10 8-10 8v-6H0z" fill="var(--orange)"/></svg>Very high tensile adhesion</li>
    <li><svg width="22" height="16" viewBox="0 0 22 16"><path d="M0 6h12V0l10 8-10 8v-6H0z" fill="var(--orange)"/></svg>Very low water absortion</li>
    <li><svg width="22" height="16" viewBox="0 0 22 16"><path d="M0 6h12V0l10 8-10 8v-6H0z" fill="var(--orange)"/></svg>No water coming needed</li>
    <li><svg width="22" height="16" viewBox="0 0 22 16"><path d="M0 6h12V0l10 8-10 8v-6H0z" fill="var(--orange)"/></svg>Very high coverage &amp; easy to apply</li>
  </ul>

  <div class="check-column">
    <div class="check-column__box"></div>
    <div class="check-column__box"></div>
    <div class="check-column__box"></div>
    <div class="check-column__box"></div>
    <div class="check-column__box"></div>
  </div>

  <footer class="maker-line">
    <span class="maker-line__label">A Premium Product from</span>
    <span class="maker-line__divider"></span>
    <span class="maker-line__name">NOVA COAT</span>
  </footer>
</main>
</body>
</html>
```